Modern, upmarket label design for food product

We need a label design for a food company producing nuts with sesame and honey. In fact, we would like the words "Cashews med sesam & honning" on the label (It's in Danish and means - Cashews with sesame & honey). It should be easy for the customer to quickly understand what it is.

It is a shelf product in the competitive food industry, which is why the design should wake the feeling of 'just wanting to grab the product down from the shelves'. So, the design should stand out and have an image of a cool, modern, hip product. This being said, I love a raw & handmade look.

The company is called Tyvo. Its origins are from the danish word Pilt that is a Danish slang for yummy. I have uploaded a photo of the package the products will be sold in.

Info & dimensions on bag in picture 1.
Dimensions: 6" x 9" | 15.2 cm x 22.3 cm
Capacity: 8 ounces | 250 grams (based on whole bean coffee)

Picture 2 is the same product, but has the possibility of attaching to a hanger on shelfs.

Picture 3 - I have also uploaded a photo of a product bag, where the hole is linear instead of a round hole. The designer chooses, which bag they will like to work with!

Please let me know if there are any questions!

Target Market(s)

Target market could really be any age, but the design needs to compel the target audience to pick it from the shelves. The package should signal a product you want to hold and have other people seeing you have it. The target audience is people who cares for what they buy, and typically doesn't want a low-end or budget product. They want the whole thing, meaning it has to taste good, look good etc. They are also the type of people who like to show off whatever products they buy by placing them in their houses for their guests to see. Or by uploading pictures of it on social medias.

Industry/Entity Type

It Company

Font styles to use
Other font styles liked:
• Not a must, but I like the 'Panton' script

Requirements
Must have
• My project must have the words 'Cashews med sesam & honning' on the label, so the customer will know within a second what they are looking at and buying.
Nice to have
• I am picturing the label with the words 'Cashews med sesam & honning' as a statement, again, emphasizing how the customer instantly should know what the product is. This being said, it should not be the only thing on the package and I love a raw & handmade look - which inspiration picture 5 is a great example of!
• I have uploaded photos of what I think looks good. With this said, I am not looking for a copy of those products, but see them as good inspiration. I have named the photos inspiration 1, 2, 3, 4 & 5.
• If needed, more text can be put on the label. For example 'vegan', 'laktosefri', Glutenfri', or 'Sund Snack' are great words for being used on the label.
Should not have
• The fonts on the label should not be too decorative. Personally I like an easy too read font.

```html
<!DOCTYPE html>
<html lang="da">
<head>
<meta charset="utf-8">
<title>Tyvo – Cashews med sesam &amp; honning</title>
<link rel="stylesheet" href="https://fonts.googleapis.com/css2?family=Raleway:wght@300;700;800;900&display=swap">
<style>
  :root {
    --kraft: #bb8f63;
    --kraft-light: #c49a6e;
    --navy: #27303f;
    --green: #1d6a3a;
    --green-dark: #155a2e;
    --white: #ffffff;
    --cream: #f3ece2;
    --nut-light: #c28a4a;
    --nut-dark: #6b4420;
  }
  html, body {
    margin: 0;
    padding: 0;
    overflow: hidden;
    background: #ffffff;
  }
  .label {
    position: relative;
    width: 800px;
    height: 1200px;
    overflow: hidden;
    background: radial-gradient(ellipse at 50% 40%, var(--kraft-light), var(--kraft) 70%);
    font-family: "Raleway", sans-serif;
  }
  .label__frame {
    position: absolute;
    left: 15px; top: 18px;
    width: 770px; height: 1166px;
    box-sizing: border-box;
    border: 5px solid var(--navy);
    border-radius: 30px;
  }
  .label__stitch {
    position: absolute;
    left: 30px; top: 30px;
    width: 740px; height: 1140px;
    box-sizing: border-box;
    border: 4px dashed var(--white);
    border-radius: 26px;
  }
  .brand-name {
    position: absolute;
    left: 0; right: 0; top: 196px;
    margin: 0;
    text-align: center;
    font-weight: 900;
    font-size: 214px;
    line-height: 1;
    letter-spacing: 4px;
    color: var(--navy);
  }
  .flourish {
    position: absolute;
    left: 236px; top: 396px;
    width: 328px; height: 50px;
    border-radius: 25px;
    background: linear-gradient(90deg, rgba(255,255,255,0.55), rgba(255,255,255,0.9), rgba(255,255,255,0.55));
  }
  .ribbon {
    position: absolute;
    left: 88px; top: 566px;
    width: 626px; height: 100px;
  }
  .product-name {
    position: absolute;
    left: 0; right: 0; top: 578px;
    margin: 0;
    text-align: center;
    font-weight: 800;
    font-size: 62px;
    line-height: 1;
    color: var(--white);
  }
  .product-flavour {
    position: absolute;
    left: 0; right: 0; top: 646px;
    margin: 0;
    text-align: center;
    font-weight: 300;
    font-size: 38px;
    line-height: 1;
    letter-spacing: 1px;
    color: var(--cream);
  }
  .claim-tag {
    position: absolute;
    left: 253px; top: 729px;
    width: 294px; height: 47px;
  }
  .claim-text {
    position: absolute;
    left: 253px; top: 729px;
    width: 294px; height: 47px;
    margin: 0;
    text-align: center;
    font-weight: 700;
    font-size: 33px;
    line-height: 47px;
    color: var(--white);
  }
  .product-window {
    position: absolute;
    left: 46px; top: 794px;
    width: 709px; height: 210px;
    box-sizing: border-box;
    border: 7px solid var(--navy);
    border-radius: 26px;
    background: radial-gradient(ellipse at 50% 50%, var(--nut-light), #a8703a 55%, var(--nut-dark));
  }
  .net-weight {
    position: absolute;
    left: 0; right: 0; top: 1052px;
    margin: 0;
    text-align: center;
    font-weight: 700;
    font-size: 34px;
    line-height: 1;
    color: var(--white);
  }
</style>
</head>
<body>
  <main class="label">
    <div class="label__frame"></div>
    <div class="label__stitch"></div>

    <h1 class="brand-name">TYVO</h1>
    <div class="flourish" role="img" aria-label="Decorative white scroll flourish"></div>

    <svg class="ribbon" viewBox="0 0 626 100" aria-hidden="true">
      <polygon class="ribbon__tail" points="0,24 70,24 70,96 0,96 24,60" fill="var(--green-dark)"/>
      <polygon class="ribbon__tail" points="626,24 556,24 556,96 626,96 602,60" fill="var(--green-dark)"/>
      <rect class="ribbon__band" x="60" y="5" width="506" height="76" rx="4" fill="var(--green)"/>
    </svg>
    <h2 class="product-name">CASHEWS MED</h2>
    <p class="product-flavour">SESAM &amp; HONNING</p>

    <svg class="claim-tag" viewBox="0 0 294 47" aria-hidden="true">
      <polygon points="0,0 294,0 284,23.5 294,47 0,47 10,23.5" fill="var(--navy)"/>
    </svg>
    <p class="claim-text">Sund Snack</p>

    <div class="product-window" role="img" aria-label="Photo of golden nut pieces"></div>

    <p class="net-weight">8 ounces | 250 grams</p>
  </main>
</body>
</html>
```